Beacon Advisory Website

I currently have a website www.beaconadvisoryinc.example. We are a IT Consulting Company. Our website will pretty much tell out our services. I am looking to enhance my website and make it look more professional. Looking for very classy and Contemporary look and design for my website.

Industry/Entity Type

It Company

```html
<!DOCTYPE html>
<html lang="en">
<head>
<meta charset="utf-8">
<title>Beacon Advisory</title>
<link href="https://fonts.googleapis.com/css2?family=Figtree:ital,wght@0,400;0,500;0,600;0,700;0,800;1,400&display=swap" rel="stylesheet">
<style>
:root{
  --blue:#1b5ea8;
  --blue-deep:#14508f;
  --blue-hero:#2c6db4;
  --orange:#f26a2e;
  --ink:#222;
  --grey:#777;
  --white:#fff;
  --line:rgba(255,255,255,.45);
}
*{margin:0;padding:0;box-sizing:border-box}
html,body{width:1200px;height:2985px;overflow:hidden}
body{font-family:"Figtree",Arial,sans-serif;color:var(--ink);position:relative;background:var(--white)}
.abs{position:absolute}

/* hero */
.hero{position:absolute;left:0;top:0;width:1200px;height:613px;overflow:hidden}
.hero-photo{position:absolute;inset:0;background:linear-gradient(110deg,#3e7cc0 0%,#2a68ad 40%,#1f5698 70%,#2f6fb4 100%)}
.brand{left:40px;top:18px;display:flex;align-items:center;gap:10px;color:var(--white);font-weight:700;font-size:22px;letter-spacing:.5px}
.brand-mark{width:30px;height:30px;border-radius:50%;background:var(--white)}
.nav{left:535px;top:30px;display:flex;gap:0;color:var(--white);font-size:12px;font-weight:500;text-transform:uppercase}
.nav span{margin-right:26px}
.join{left:1055px;top:22px;width:107px;height:30px;background:var(--blue);color:var(--white);font-size:12px;display:flex;align-items:center;justify-content:center}
.dropdown{left:533px;top:60px;width:116px;height:109px;background:var(--white);padding-top:8px;font-size:13px}
.dropdown div{height:32px;line-height:32px;padding-left:18px;color:#333}
.dropdown .active{background:#e8ecf2}
.hero-title{left:120px;top:226px;font-size:44px;font-weight:800;color:var(--white);letter-spacing:.5px}
.hero-text{left:120px;top:286px;width:390px;font-size:14px;line-height:18px;color:var(--white)}
.cta{left:120px;top:366px;width:218px;height:48px}
.cta-label{left:148px;top:380px;color:var(--white);font-weight:700;font-size:16px}

/* about */
.about-title{left:120px;top:796px;font-size:30px;font-weight:500}
.about-text{left:120px;top:852px;width:475px;font-size:13.5px;line-height:16.5px}
.btn{position:absolute;background:var(--orange);color:var(--white);font-size:11px;text-transform:uppercase;display:flex;align-items:center;justify-content:center}
.laptop{left:577px;top:726px;width:623px;height:398px}

/* services */
.services{position:absolute;left:0;top:1234px;width:1200px;height:696px;background:radial-gradient(ellipse at 50% 40%,#2065b0 0%,var(--blue) 55%,var(--blue-deep) 100%)}
.svc-title{position:absolute;color:var(--white);font-size:16px;font-weight:500}
.svc-text{position:absolute;width:270px;color:var(--white);font-size:13.5px;line-height:18px}
.right{text-align:right}

/* team */
.team-title{left:0;width:1200px;top:2002px;text-align:center;font-size:26px;font-weight:500}
.team-photo{left:191px;top:2090px;width:404px;height:404px}
.member-name{left:633px;top:2090px;font-size:27px;font-style:italic;color:var(--blue)}
.member-role{left:633px;top:2140px;font-size:13px;font-style:italic;color:var(--grey);line-height:24px}
.member-bio{left:633px;top:2201px;width:400px;font-size:14px;line-height:16px}
.thumb{position:absolute;top:2385px;width:62px;height:62px;background:linear-gradient(#4d82bd,#2c68ab)}

/* footer */
.footer{position:absolute;left:0;top:2594px;width:1200px;height:391px;background:var(--blue);color:var(--white)}
.fcol{position:absolute;top:60px}
.fcol h4{font-size:16px;font-weight:500;margin-bottom:17px}
.fcol li{list-style:none;font-size:11.5px;line-height:27px}
.subscribe{left:860px;top:60px;width:240px;font-size:16px;line-height:22px;font-weight:500}
.email{left:860px;top:121px;width:221px;height:34px;background:var(--white);color:#999;font-size:11px;padding-left:12px;line-height:34px}
.follow{left:120px;top:332px;font-size:16px;display:flex;align-items:center;gap:14px}
.social{width:14px;height:14px;border-radius:50%;background:var(--white)}
.copy{left:358px;top:337px;font-size:11px}
</style>
</head>
<body>

<header class="hero">
  <div class="hero-photo" role="img" aria-label="Photo of two consultants shaking hands over a laptop, tinted blue"></div>
  <div class="abs brand"><span class="brand-mark"></span>BEACON ADVISORY</div>
  <nav class="abs nav"><span>Company</span><span>Services</span><span>Solutions</span><span>Resources</span><span>Career</span><span>Contact Us</span></nav>
  <div class="abs join">JOIN US FREE</div>
  <div class="abs dropdown"><div>What we do</div><div class="active">Our Process</div><div>Who we are</div></div>
  <h1 class="abs hero-title">CONSULTING</h1>
  <p class="abs hero-text">Beacon Advisory has certified professional consultants to work with you to help increase the business by providing IT services</p>
  <svg class="abs cta" viewBox="0 0 218 48"><polygon points="0,0 196,0 218,24 196,48 0,48" fill="#f26a2e"/><circle cx="179" cy="24" r="8" fill="none" stroke="#fff" stroke-width="2"/><polyline points="175,24 178,27 183,21" fill="none" stroke="#fff" stroke-width="2"/></svg>
  <span class="abs cta-label">Get Started Now</span>
</header>

<section>
  <h2 class="abs about-title">About Us</h2>
  <p class="abs about-text">Today’s IT market is a dynamic, fast-paced industry, with ever-increasing demands. Meeting these demands for over 25 years, Beacon Advisory maintains a global presence, aggressively recruiting expertly qualified IT and Management Professionals from around the world and cultivating key partnerships with corporations to understand their business models end-to-end, with a goal of delivering exceptional client service and ensuring a consistent delivery of the talent needed to drive results.</p>
  <div class="btn" style="left:122px;top:1025px;width:107px;height:26px">Learn More</div>
  <div class="abs laptop" role="img" aria-label="Laptop showing a photo of a woman working at a computer" style="background:linear-gradient(#e9eaec,#d4d6da)"></div>
</section>

<section class="services">
  <svg class="abs" style="left:0;top:0" width="1200" height="696">
    <line x1="422" y1="121" x2="776" y2="121" stroke="rgba(255,255,255,.45)" stroke-width="1.5"/>
    <line x1="599" y1="121" x2="599" y2="513" stroke="rgba(255,255,255,.45)" stroke-width="1.5"/>
    <g fill="none" stroke="#fff" stroke-width="2">
      <circle cx="502" cy="223" r="70"/><circle cx="698" cy="223" r="70"/>
      <circle cx="502" cy="414" r="70"/><circle cx="698" cy="414" r="70"/>
    </g>
    <!-- gear -->
    <g transform="translate(502 223)" fill="#fff">
      <g id="teeth">
        <rect x="-5" y="-26" width="10" height="12"/><rect x="-5" y="14" width="10" height="12"/>
        <rect x="-26" y="-5" width="12" height="10"/><rect x="14" y="-5" width="12" height="10"/>
      </g>
      <g transform="rotate(45)"><rect x="-5" y="-26" width="10" height="12"/><rect x="-5" y="14" width="10" height="12"/><rect x="-26" y="-5" width="12" height="10"/><rect x="14" y="-5" width="12" height="10"/></g>
      <circle r="17"/><circle r="7" fill="#1b5ea8"/>
    </g>
    <!-- handshake -->
    <g transform="translate(698 223)" fill="#fff">
      <rect x="-40" y="-20" width="14" height="26" transform="rotate(-30 -33 -7)"/>
      <rect x="26" y="-20" width="14" height="26" transform="rotate(30 33 -7)"/>
      <path d="M-24 -8 L-4 -18 L14 -10 L24 -4 L20 14 L4 24 L-12 14 Z"/>
      <path d="M-6 -6 L6 4 M2 -10 L14 0" stroke="#1b5ea8" stroke-width="3"/>
    </g>
    <!-- phone -->
    <g transform="translate(502 414)">
      <rect x="-13" y="-24" width="26" height="48" rx="4" fill="none" stroke="#fff" stroke-width="3"/>
      <circle cy="17" r="2.5" fill="#fff"/>
    </g>
    <!-- factory -->
    <g transform="translate(698 414)" fill="#fff">
      <rect x="4" y="-28" width="8" height="18"/>
      <path d="M-26 24 L-26 -4 L-12 -14 L-12 -4 L2 -14 L2 -4 L16 -14 L24 -14 L24 24 Z"/>
      <rect x="-4" y="8" width="10" height="16" fill="#1b5ea8"/>
    </g>
  </svg>
  <div class="svc-title right" style="left:112px;width:270px;top:176px">Technology</div>
  <p class="svc-text right" style="left:112px;top:202px">Lorem ipsum dolor sit amet, consectetur adipisicing elit, sed do eiusmod tempor incididunt ut labore</p>
  <div class="svc-title" style="left:816px;top:176px">Offshore Business</div>
  <p class="svc-text" style="left:816px;top:202px">Lorem ipsum dolor sit amet, consectetur adipisicing elit, sed do eiusmod tempor incididunt ut labore</p>
  <div class="svc-title right" style="left:112px;width:270px;top:366px">Application Developement</div>
  <p class="svc-text right" style="left:112px;top:392px">Lorem ipsum dolor sit amet, consectetur adipisicing elit, sed do eiusmod tempor incididunt ut labore</p>
  <div class="svc-title" style="left:810px;top:366px">Enterprise Integration</div>
  <p class="svc-text" style="left:810px;top:392px">Lorem ipsum dolor sit amet, consectetur adipisicing elit, sed do eiusmod tempor incididunt ut labore</p>
  <div class="btn" style="left:543px;top:571px;width:114px;height:32px">Learn More</div>
</section>

<section>
  <h2 class="abs team-title">Our Team</h2>
  <div class="abs team-photo" role="img" aria-label="Portrait photo of a smiling team member in glasses and suit" style="background:linear-gradient(#d8d8d6,#b9bab8)"></div>
  <div class="abs member-name">Marcus Hale</div>
  <div class="abs member-role">Executive Director<br>beaconadvisoryinc.example</div>
  <p class="abs member-bio">Lorem ipsum dolor sit amet, consectetur adipisicing elit, sed do eiusmod incididunt ut labore et dolore magna aliqua. Lorem ipsum dolor sit amet, consectetur adipisicing elit, sed do eiusmod incididunt ut labore et dolore magna aliqua.</p>
  <svg class="abs" style="left:630px;top:2254px" width="120" height="44">
    <circle cx="8" cy="22" r="5" fill="#999"/><line x1="27" y1="4" x2="27" y2="40" stroke="#ccc"/>
    <circle cx="48" cy="22" r="5" fill="#999"/><line x1="67" y1="4" x2="67" y2="40" stroke="#ccc"/>
    <circle cx="90" cy="22" r="5" fill="#999"/>
  </svg>
  <div class="thumb" role="img" aria-label="Team member portrait" style="left:631px"></div>
  <div class="thumb" role="img" aria-label="Team member portrait" style="left:701px;background:linear-gradient(#e4e4e2,#c7c7c5)"></div>
  <div class="thumb" role="img" aria-label="Team member portrait" style="left:771px"></div>
  <div class="thumb" role="img" aria-label="Team member portrait" style="left:841px"></div>
</section>

<footer class="footer">
  <div class="fcol" style="left:120px"><h4>About us</h4><ul><li>Company</li><li>Services</li><li>Solution</li><li>Resources</li><li>Career</li><li>Contact Us</li></ul></div>
  <div class="fcol" style="left:303px"><h4>Services</h4><ul><li>Technology</li><li>Offshore Business</li><li>Application Developement</li><li>Enterprise Integration</li><li>IT Consulting</li></ul></div>
  <div class="fcol" style="left:516px"><h4>Solutions</h4><ul><li>Dashboard</li><li>Wherehouseing</li><li>BPM</li></ul></div>
  <div class="fcol" style="left:679px"><h4>Resources</h4><ul><li>Our Process</li><li>Staff Augmentation</li></ul></div>
  <div class="abs subscribe">Submit your e-mail receive back details within 24 hours</div>
  <div class="abs email">Enter your email id</div>
  <div class="btn" style="left:860px;top:171px;width:113px;height:34px">Subscribe</div>
  <div class="abs follow">Follow us <span class="social"></span><span class="social"></span><span class="social"></span><span class="social"></span></div>
  <div class="abs copy">© 2015</div>
</footer>

</body>
</html>
```